Bookcover: Lessons From the Silent Orchard

I am publishing a super-low-cost innovation book for €4,99 on Bravolo Self Release to help everyone become a great innovator: young ambitious people without college education nor a big budget. Do you want to help me?

Brief:
Design a book cover 1600 x 2560 pixels for BSR.
Main title: Lessons From the Silent Orchard
Sub title: mindset - insights - skills & tools
Author: Maarten de Klerk
Design: captive, and appealing to everyone
Target Group: young ambitious people without college education

For bravolo please format the height/width ratio of 1.6:1

```html
<!DOCTYPE html>
<html lang="en">
<head>
<meta charset="utf-8">
<title>Lessons From the Silent Orchard – Book Cover</title>
<link rel="stylesheet" href="https://fonts.googleapis.com/css2?family=Oswald:wght@500;600;700&display=swap">
<style>
  :root {
    --page-bg: #ececec;
    --cover-bg: #ffffff;
    --ink: #1f1f33;
    --accent: #f29a2e;
    --band-text: #ffffff;
    --art-warm: #f7c23a;
    --art-orange: #f0912f;
    --art-teal: #7ccbd6;
    --art-floor: #4fb3c6;
    --art-blue: #2f5fa8;
    --art-green: #1fa370;
    --art-red: #d6513a;
  }
  * { margin: 0; padding: 0; box-sizing: border-box; }
  html, body {
    width: 1199px;
    height: 1200px;
    overflow: hidden;
    background: var(--page-bg);
  }
  .cover {
    position: absolute;
    left: 279px;
    top: 88px;
    width: 640px;
    height: 1024px;
    background: var(--cover-bg);
    font-family: "Oswald", "Arial Narrow", sans-serif;
    color: var(--ink);
    overflow: hidden;
  }
  .title-line {
    position: absolute;
    left: 0;
    width: 100%;
    text-align: center;
    text-transform: uppercase;
    font-weight: 700;
    line-height: 1;
    letter-spacing: -1px;
    white-space: nowrap;
  }
  .title-line span {
    display: inline-block;
    transform: scaleX(0.9);
  }
  .title-lead { top: 55px; font-size: 75px; }
  .title-main { top: 126px; font-size: 92px; }
  .cover-art {
    position: absolute;
    left: 47px;
    top: 253px;
    width: 550px;
    height: 528px;
  }
  .cover-subtitle {
    position: absolute;
    top: 802px;
    left: 0;
    width: 100%;
    text-align: center;
    font-size: 40px;
    font-weight: 600;
    letter-spacing: -1px;
    white-space: nowrap;
  }
  .cover-subtitle .sep {
    color: var(--accent);
    margin: 0 8px;
  }
  .author-band {
    position: absolute;
    left: 0;
    bottom: 0;
    width: 100%;
    height: 78px;
    background: var(--ink);
    display: flex;
    align-items: center;
    justify-content: center;
  }
  .author-name {
    color: var(--band-text);
    font-size: 42px;
    font-weight: 600;
    letter-spacing: -0.5px;
    line-height: 1;
    display: inline-block;
    transform: scaleX(0.92);
  }
</style>
</head>
<body>
  <div class="cover">
    <h1>
      <span class="title-line title-lead"><span>Lessons From the</span></span>
      <span class="title-line title-main"><span>Silent Orchard</span></span>
    </h1>

    <svg class="cover-art" viewBox="0 0 550 528" role="img"
         aria-label="Illustration of a large glowing yellow and orange light bulb with four people in colourful clothes gathered around it sharing ideas, with clouds, sparkles and check-mark bubbles">
      <defs>
        <radialGradient id="art-bulb" cx="50%" cy="40%" r="42%">
          <stop offset="0%" stop-color="var(--art-warm)"/>
          <stop offset="55%" stop-color="var(--art-orange)" stop-opacity="0.9"/>
          <stop offset="100%" stop-color="var(--art-orange)" stop-opacity="0"/>
        </radialGradient>
        <linearGradient id="art-sky" x1="0" y1="0" x2="0" y2="1">
          <stop offset="0%" stop-color="#eaf6f8"/>
          <stop offset="60%" stop-color="#fdf3e2"/>
          <stop offset="100%" stop-color="#e3f2f5"/>
        </linearGradient>
        <linearGradient id="art-people" x1="0" y1="0" x2="1" y2="0">
          <stop offset="0%" stop-color="var(--art-green)" stop-opacity="0.55"/>
          <stop offset="25%" stop-color="var(--art-red)" stop-opacity="0.5"/>
          <stop offset="50%" stop-color="var(--art-blue)" stop-opacity="0.45"/>
          <stop offset="75%" stop-color="var(--art-green)" stop-opacity="0.5"/>
          <stop offset="100%" stop-color="var(--art-blue)" stop-opacity="0.55"/>
        </linearGradient>
        <linearGradient id="art-fade" x1="0" y1="0" x2="0" y2="1">
          <stop offset="0%" stop-color="#fff" stop-opacity="0"/>
          <stop offset="100%" stop-color="#fff" stop-opacity="1"/>
        </linearGradient>
        <mask id="art-people-mask">
          <rect x="0" y="330" width="550" height="180" fill="url(#art-fade)"/>
        </mask>
      </defs>
      <rect x="0" y="0" width="550" height="528" rx="18" fill="url(#art-sky)"/>
      <rect x="0" y="20" width="550" height="460" fill="url(#art-bulb)"/>
      <rect x="0" y="330" width="550" height="180" fill="url(#art-people)" mask="url(#art-people-mask)"/>
      <rect x="14" y="490" width="522" height="26" rx="13" fill="var(--art-floor)" opacity="0.7"/>
    </svg>

    <p class="cover-subtitle">Mindset<span class="sep">-</span>Insights<span class="sep">-</span>Skills &amp; Tools</p>

    <div class="author-band">
      <span class="author-name">Maarten de Klerk</span>
    </div>
  </div>
</body>
</html>
```